Bright Sprout Learning Centre website redesign

Our website (which we have only just converted to wordpress) is just not good enough for my liking. Our centre offers classes for babies aged from 6 months to 7 years old in the middle east. Whilst our program is formal in the way that the practise deals with learning in hemispheres of the brain - the site should look more fun and a bit more approachable and attractive to families.
I like the site www.tallowpine.com or www.corvidlane.com from this region - I like the way that you land on home page with images and a quote rather than all this information coming at you and you not knowing where to click.
I want a fun and appealing site that features info about the program, class timetable, shop, news and events, gallery, blog posts etc…
I am really open to a complete redesign and just want something that looks professional but is fun and gets the information out quickly! Please look at www.brightsprout.ae for current site design

```html
<!DOCTYPE html>
<html lang="en">
<head>
<meta charset="utf-8">
<title>Bright Sprout Learning Centre</title>
<link rel="stylesheet" href="https://fonts.googleapis.com/css2?family=Open+Sans:wght@400;600;700&family=Noto+Serif:wght@400&display=swap">
<style>
:root{
  --orange:#e8692f;
  --orange-soft:#f58b5c;
  --orange-deep:#df7048;
  --sky:#3aa9d8;
  --nav:#2a9fd6;
  --cream:#fdf1cf;
  --sand:#f1d98a;
  --pink:#ef7f80;
  --gold:#eab84a;
  --ink:#333333;
  --grey:#777777;
  --line:#ffffff;
  --teal:#4e8f8a;
}
*{margin:0;padding:0;box-sizing:border-box}
html,body{width:1200px;height:2293px;overflow:hidden}
body{position:relative;font-family:"Open Sans",Arial,sans-serif;color:var(--ink);background:#fff}
.abs{position:absolute}

/* top bar */
.topbar{left:0;top:0;width:1200px;height:38px;background:var(--orange)}
.topbar-item{top:0;height:38px;display:flex;align-items:center;gap:7px;color:#fff;font-size:12px;padding:0 14px;border-left:1px solid rgba(255,255,255,.35)}
.topbar-item svg{width:12px;height:12px}

/* header */
.header{left:0;top:38px;width:1200px;height:187px;background:#fff;border-bottom:2px dashed #eee}
.brand{left:100px;top:70px;width:140px;height:140px;display:flex;flex-direction:column;align-items:center;justify-content:center;gap:10px}
.brand-mark{width:60px;height:60px;border-radius:50%;background:#8fc3d9}
.brand-name{font-size:14px;font-weight:700;color:#4a8bb0;text-align:center;line-height:1.2}
.social{top:95px;width:40px;height:40px;border-radius:50%}
.nav{left:390px;top:154px;display:flex;align-items:center;height:39px}
.nav a{font-size:12px;color:var(--nav);text-decoration:none;margin-right:32px}
.nav a.current{background:#f0892f;color:#fff;font-weight:700;padding:0 19px;height:39px;line-height:37px;border-radius:3px;margin-right:25px;box-shadow:0 2px 0 #c8651b}

/* hero */
.hero{left:0;top:225px;width:1200px;height:642px;background:radial-gradient(ellipse at 60% 30%,#f9c24a 0%,#f08a3a 35%,#d8457a 75%,#b2307a 100%)}
.frame{left:130px;top:280px;width:936px;height:518px;border-radius:10px;background:linear-gradient(#f3d497,#d9a964);box-shadow:0 6px 12px rgba(0,0,0,.25)}
.photo{left:153px;top:301px;width:891px;height:474px;background:linear-gradient(100deg,#c9b9a4,#f4e5d5 45%,#d8c3d8 80%,#a98fc2)}
.arrow{top:515px;width:50px;height:50px;background:#d8883a;display:flex;align-items:center;justify-content:center}
.arrow svg{width:20px;height:20px}

/* blog */
.blog{left:0;top:867px;width:1200px;height:547px;background:var(--cream);border-top:2px solid #f6d9a8}
.section-title{font-size:30px;color:var(--sky);font-weight:400}
.date-tile{width:100px;display:flex;align-items:center;justify-content:center;color:#fff}
.date-day{font-family:"Noto Serif",Georgia,serif;font-style:normal;font-size:30px}
.date-meta{font-size:11px;line-height:1.1;margin-left:5px}
.post-image{height:145px;background:linear-gradient(90deg,#f5e6d9,#e9c5a2 45%,#9cc4df 75%,#f2d6de)}
.post-body{background:#fff;padding:22px 16px 0}
.post-title{font-family:"Noto Serif",Georgia,serif;font-size:20px;color:#333;margin-bottom:18px;font-weight:400}
.post-text{font-size:12px;color:var(--grey);line-height:22px}
.post-foot{height:38px;background:var(--sand);display:flex;align-items:center;gap:14px;padding-left:20px;font-size:12px;color:#777}

/* news */
.news-title{left:157px;top:1477px;font-size:27px;color:#3d8fb0;font-weight:400}
.news-icon{left:100px;top:1473px;width:45px;height:40px;border-radius:50%;background:linear-gradient(#f1c84c,#7cba4b)}
.news-item{left:101px;width:300px}
.news-item h3{font-size:14px;font-weight:700;color:var(--sky);margin-bottom:2px}
.news-item p{font-size:13px;font-weight:600;line-height:20px;color:#222}
.divider{left:418px;top:1475px;width:2px;height:291px;background:#eee}
.card{width:183px;height:270px;background:#fff;border:1px solid #e2e2e2;border-radius:4px;box-shadow:0 10px 12px -6px rgba(0,0,0,.15);padding:12px 10px}
.card h4{font-size:19px;font-weight:700;text-align:center;color:#111;margin-bottom:6px}
.card-img{height:78px;margin-bottom:10px}
.card p{font-size:11px;font-weight:600;line-height:18px;color:#222}

/* footer */
.footer{left:0;top:1847px;width:1200px;height:401px;background:var(--orange-soft);border-top:4px solid var(--orange)}
.col-title{top:1891px;font-size:18px;color:#fff;font-weight:400;width:218px;padding-bottom:12px;border-bottom:3px solid var(--line)}
.thumb{width:58px;height:58px;border:3px solid #fff;border-radius:4px}
.foot-text{font-size:12px;color:#fff;line-height:22px}
.field{left:337px;width:220px;height:40px;background:#fdf2cf;border-radius:4px;font-size:12px;padding-left:12px;line-height:40px;color:#333}
.subscribe{left:463px;top:2137px;width:94px;height:40px;background:#e9b641;border-radius:4px;font-family:"Noto Serif",Georgia,serif;font-size:16px;color:#333;text-align:center;line-height:40px}
.contact-row{left:580px;display:flex;gap:10px;font-size:12px;color:#fff;align-items:flex-start}
.contact-row svg{width:16px;height:16px;flex:none;margin-top:2px}
.foot-social{top:2138px;width:40px;height:40px;border-radius:50%;background:var(--teal)}
.about-list{left:820px;top:2065px;list-style:none}
.about-list li{font-size:12px;color:#fff;line-height:22px;display:flex;align-items:center;gap:9px}
.about-list li::before{content:"";width:9px;height:9px;background:#fff;border-radius:2px}
.bottombar{left:0;top:2248px;width:1200px;height:45px;background:var(--orange-deep);display:flex;align-items:center;color:#fff;font-size:13px}
.bottom-links{position:absolute;left:507px;top:0;height:45px;display:flex;align-items:center;gap:12px}
</style>
</head>
<body>

<div class="abs topbar">
  <div class="abs topbar-item" style="left:558px">
    <svg viewBox="0 0 12 12"><path d="M3 1l2 2-1 1.5c.8 1.6 1.9 2.7 3.5 3.5L9 7l2 2-1.5 2C5 10.5 1.5 7 1 2.5z" fill="#fff"/></svg>
    Call : 888-555-0147
  </div>
  <div class="abs topbar-item" style="left:718px">
    <svg viewBox="0 0 12 12"><path d="M1 2h5v1.5H2.5v5H6V10H1z M5 4.5h4V3l3 3-3 3V7.5H5z" fill="#fff"/></svg>
    Sign in (or) Logout
  </div>
  <div class="abs topbar-item" style="left:876px;border-right:1px solid rgba(255,255,255,.35)">
    <svg viewBox="0 0 12 12"><path d="M0 1h2l1.5 6h7L12 3H4" fill="none" stroke="#fff" stroke-width="1.3"/><circle cx="4.5" cy="10" r="1.1" fill="#fff"/><circle cx="9.5" cy="10" r="1.1" fill="#fff"/></svg>
    (0) items in cart | ($0.00)
  </div>
</div>

<header class="abs header"></header>
<div class="abs brand">
  <span class="brand-mark"></span>
  <span class="brand-name">Bright Sprout<br>Learning Centre</span>
</div>
<span class="abs social" style="left:915px;background:#1f4e86" aria-label="Social link"></span>
<span class="abs social" style="left:963px;background:#2ba6de" aria-label="Social link"></span>
<span class="abs social" style="left:1011px;background:#f39323" aria-label="Feed link"></span>
<span class="abs social" style="left:1060px;background:#a7a7a7" aria-label="Email link"></span>
<nav class="abs nav">
  <a class="current">Home</a><a>The Program</a><a>Classes</a><a>Media</a><a>Our Location</a><a>Blog</a><a>About Us</a><a>Shop</a><a>Contact Us</a>
</nav>

<section class="abs hero"></section>
<div class="abs frame"></div>
<div class="abs photo" role="img" aria-label="Three smiling children giving thumbs up in a bright classroom"></div>
<div class="abs arrow" style="left:80px"><svg viewBox="0 0 20 20"><path d="M13 3L6 10l7 7" fill="none" stroke="#fff" stroke-width="3"/></svg></div>
<div class="abs arrow" style="left:1068px"><svg viewBox="0 0 20 20"><path d="M7 3l7 7-7 7" fill="none" stroke="#fff" stroke-width="3"/></svg></div>

<section class="abs blog"></section>
<h2 class="abs section-title" style="left:116px;top:925px">Blog Posts</h2>

<!-- post one -->
<div class="abs date-tile" style="left:115px;top:983px;height:45px;background:var(--sky)"><span class="date-day">20</span><span class="date-meta">Jul<br>2013</span></div>
<div class="abs date-tile" style="left:115px;top:1028px;height:52px;background:var(--pink);font-size:16px">1 &#9679;</div>
<div class="abs date-tile" style="left:115px;top:1080px;height:48px;background:var(--gold)"><svg width="16" height="18" viewBox="0 0 16 18"><path d="M2 1h8l4 4v12H2z" fill="#fff"/></svg></div>
<div class="abs post-image" style="left:214px;top:983px;width:359px" role="img" aria-label="Child painting a colourful rainbow picture"></div>
<article class="abs post-body" style="left:214px;top:1128px;width:359px;height:172px">
  <h3 class="post-title">Activities Improves Mind</h3>
  <p class="post-text">Roin bibendum nibhsds. Nuncsdsd fermdada msit ametadasd consequat. Praes porr nulla sit amet dui lobortis, id venenatis nibh accumsan....</p>
</article>
<div class="abs post-foot" style="left:214px;top:1300px;width:359px"><span>&#9679; Mira</span><span>&#9679; Tour</span></div>

<!-- post two -->
<div class="abs date-tile" style="left:593px;top:983px;height:45px;background:var(--sky)"><span class="date-day">08</span><span class="date-meta">Jul<br>2013</span></div>
<div class="abs date-tile" style="left:593px;top:1028px;height:52px;background:var(--pink);font-size:16px">2 &#9679;</div>
<div class="abs date-tile" style="left:593px;top:1080px;height:48px;background:var(--gold)"><svg width="20" height="16" viewBox="0 0 20 16"><rect x="1" y="3" width="18" height="12" rx="2" fill="#fff"/><circle cx="10" cy="9" r="3.5" fill="var(--gold)"/></svg></div>
<div class="abs post-image" style="left:693px;top:983px;width:359px" role="img" aria-label="Child painting a colourful rainbow picture"></div>
<article class="abs post-body" style="left:693px;top:1128px;width:359px;height:176px">
  <h3 class="post-title">Weekly Reader Zone</h3>
  <p class="post-text">Curabitur ultrices posuere mattis. Nam ullamcorper, diam sit amet euismod pellentesque, eros risus rhoncus libero, in vestibulum nisl ligula...</p>
</article>
<div class="abs post-foot" style="left:693px;top:1304px;width:359px"><span>&#9679; Mira</span><span>&#9679; Tour</span><span>&#9679; Activity</span></div>

<!-- news -->
<div class="abs news-icon" role="img" aria-label="Small snail illustration"></div>
<h2 class="abs news-title">News &amp; Events</h2>
<div class="abs news-item" style="top:1527px"><h3>Impact of the Carbon Price &amp; Carbon</h3><p>Thursday 10 November - Afternoon Conference.<br>Registration fee includes lunch.</p></div>
<div class="abs news-item" style="top:1605px"><h3>Impact of the Carbon Price &amp; Carbon</h3><p>Thursday 10 November - Afternoon Conference.<br>Registration fee includes lunch.</p></div>
<div class="abs news-item" style="top:1689px"><h3>Impact of the Carbon Price &amp; Carbon</h3><p>Thursday 10 November - Afternoon Conference.<br>Registration fee includes lunch.</p></div>
<div class="abs divider"></div>

<div class="abs card" style="left:446px;top:1489px">
  <h4>Lorem Ipsum</h4>
  <div class="card-img" style="background:linear-gradient(90deg,#efe3dc,#c7dcb0)" role="img" aria-label="Baby playing with a soft toy"></div>
  <p>simply dummy text of the printing and typesetting industry. Lorem Ipsum has been the industry's standard when an un known printer took a galley</p>
</div>
<div class="abs card" style="left:677px;top:1489px">
  <h4>Lorem Ipsum</h4>
  <div class="card-img" style="background:linear-gradient(90deg,#e7eef3,#d9b39a)" role="img" aria-label="Teacher with a group of children"></div>
  <p>simply dummy text of the printing and typesetting industry. Lorem Ipsum has been the industry's standard when an un known printer took a galley</p>
</div>
<div class="abs card" style="left:913px;top:1493px">
  <h4>Lorem Ipsum</h4>
  <div class="card-img" style="background:linear-gradient(90deg,#d9b08d,#b86a4d)" role="img" aria-label="Teacher reading with children"></div>
  <p>simply dummy text of the printing and typesetting industry. Lorem Ipsum has been the industry's standard when an un known printer took a galley</p>
</div>

<!-- footer -->
<footer class="abs footer"></footer>
<h3 class="abs col-title" style="left:100px">Gallery</h3>
<h3 class="abs col-title" style="left:336px">Signup Newsletter</h3>
<h3 class="abs col-title" style="left:580px">Contact Us</h3>
<h3 class="abs col-title" style="left:820px">About Us</h3>

<div class="abs thumb" style="left:100px;top:1971px;background:#bfd9ea" role="img" aria-label="Gallery photo of children"></div>
<div class="abs thumb" style="left:179px;top:1971px;background:#d9c7c9" role="img" aria-label="Gallery photo of children"></div>
<div class="abs thumb" style="left:258px;top:1971px;background:#e8c0b4" role="img" aria-label="Gallery photo of children"></div>
<div class="abs thumb" style="left:100px;top:2052px;background:#e9d4c4" role="img" aria-label="Gallery photo of a child"></div>
<div class="abs thumb" style="left:179px;top:2052px;background:#e4b9ad" role="img" aria-label="Gallery photo of children"></div>
<div class="abs thumb" style="left:258px;top:2052px;background:#c99a86" role="img" aria-label="Gallery photo of children"></div>
<div class="abs thumb" style="left:100px;top:2133px;background:#e6b7a0" role="img" aria-label="Gallery photo of a child"></div>
<div class="abs thumb" style="left:179px;top:2133px;background:#dbe2e8" role="img" aria-label="Gallery photo of a child"></div>
<div class="abs thumb" style="left:258px;top:2133px;background:#e3c2b6" role="img" aria-label="Gallery photo of a child"></div>

<p class="abs foot-text" style="left:340px;top:1963px;width:220px">Enter your name and email address to subscribe to our Newsletter.</p>
<div class="abs field" style="top:2027px">Enter Name</div>
<div class="abs field" style="top:2082px">Enter Email</div>
<div class="abs subscribe">Subscribe</div>

<div class="abs contact-row" style="top:1968px;width:220px">
  <svg viewBox="0 0 16 16"><path d="M8 1a5 5 0 0 1 5 5c0 4-5 9-5 9S3 10 3 6a5 5 0 0 1 5-5z" fill="#fff"/><circle cx="8" cy="6" r="2" fill="var(--orange-soft)"/></svg>
  <span><b>Address:</b> 42, C Block, Palm Row, Dubai, UAE</span>
</div>
<div class="abs contact-row" style="top:2024px">
  <svg viewBox="0 0 16 16"><path d="M4 1l3 3-1.5 2c1 2 2.5 3.5 4.5 4.5L12 9l3 3-2 2.5C7 14 2 9 1.5 3z" fill="#fff"/></svg>
  <span><b>Phone:</b> 04 555 0192</span>
</div>
<div class="abs contact-row" style="top:2063px">
  <svg viewBox="0 0 16 16"><rect x="1" y="3" width="14" height="10" fill="#fff"/><path d="M1 3l7 6 7-6" fill="none" stroke="var(--orange-soft)" stroke-width="1.5"/></svg>
  <span><b>Mail:</b> hello@brightsprout.ae</span>
</div>
<p class="abs foot-text" style="left:580px;top:2105px;font-weight:700">We are Social:</p>
<span class="abs foot-social" style="left:580px" aria-label="Social link"></span>
<span class="abs foot-social" style="left:628px" aria-label="Social link"></span>
<span class="abs foot-social" style="left:677px" aria-label="Social link"></span>
<span class="abs foot-social" style="left:726px" aria-label="Social link"></span>

<p class="abs foot-text" style="left:820px;top:1963px;width:225px"><b>Sunny Steps</b> comes with powerful theme options, which empowers you to quickly and easily build incredible store.</p>
<ul class="abs about-list">
  <li>Manage Appearance</li>
  <li>Slider Manager</li>
  <li>Currency Converter</li>
  <li>Lot of HTML Styles</li>
  <li>Unique News Page Design</li>
</ul>

<div class="abs bottombar">
  <span style="margin-left:93px">&copy; Copyright Bright Sprout Learning Centre.</span>
  <div class="bottom-links"><span>Home</span>/<span>Staff</span>/<span>Shop</span>/<span>About</span>/<span>Features</span>/<span>Blog</span>/<span>Shortcodes</span>/<span>Contact</span></div>
</div>

</body>
</html>
```